" Temos como objetivo melhor atender as demandas atuais em TI com suporte de fácil acesso e analistas especializados com certificações que o mercado atual exige. Nossa equipe se dedica à prevenção, resolução de problemas e sugestões de melhorias do ambiente para garantir que seus servidores e aplicações estejam sempre no ar e funcionando, garantindo a continuidade dos negócios, foco das nossas soluções. "

```html
<!DOCTYPE html>
<html lang="pt-BR">
<head>
<meta charset="UTF-8">
<title>NUVARO – Cartão de visita</title>
<link rel="stylesheet" href="https://fonts.googleapis.com/css2?family=Montserrat:wght@400;500;700&display=swap">
<style>
  :root {
    --page-bg: #e4e5e7;
    --card-white: #ffffff;
    --navy: #0f1a2c;
    --navy-text: #1d2a3f;
    --orange: #f28c1c;
    --yellow: #f9c31f;
    --muted: #4a5263;
    --light: #f4f5f7;
  }
  * { box-sizing: border-box; margin: 0; padding: 0; }
  html, body {
    width: 1200px;
    height: 1200px;
    overflow: hidden;
    background: var(--page-bg);
    font-family: "Montserrat", sans-serif;
  }
  .sheet {
    position: relative;
    width: 1200px;
    height: 1200px;
  }
  .card {
    position: absolute;
    left: 220px;
    width: 760px;
    height: 434px;
    border-radius: 24px;
    overflow: hidden;
    box-shadow: 0 10px 30px rgba(15, 26, 44, 0.18);
  }
  /* Front side */
  .card-front {
    top: 110px;
    background: var(--card-white);
  }
  .identity {
    position: absolute;
    left: 64px;
    top: 62px;
    padding-left: 14px;
    border-left: 3px solid var(--orange);
  }
  .person-name {
    font-size: 26px;
    font-weight: 700;
    letter-spacing: 0.5px;
    color: var(--orange);
    text-transform: uppercase;
    line-height: 1.15;
  }
  .person-role {
    font-size: 17px;
    font-weight: 500;
    color: var(--navy-text);
    margin-top: 4px;
  }
  .contact-list {
    position: absolute;
    left: 64px;
    top: 170px;
    list-style: none;
    display: flex;
    flex-direction: column;
    gap: 16px;
  }
  .contact-item {
    display: flex;
    align-items: flex-start;
    gap: 12px;
    font-size: 16px;
    font-weight: 500;
    color: var(--muted);
    line-height: 1.3;
  }
  .contact-icon {
    flex: 0 0 24px;
    width: 24px;
    height: 24px;
  }
  .brand-accent {
    position: absolute;
    right: 40px;
    bottom: 40px;
    width: 300px;
    height: 300px;
    border-radius: 50%;
    background: linear-gradient(135deg, var(--yellow), var(--orange));
  }
  /* Back side */
  .card-back {
    top: 640px;
    background: var(--navy);
    display: flex;
    align-items: center;
    justify-content: center;
  }
  .brand-lockup {
    display: flex;
    align-items: center;
    gap: 26px;
  }
  .brand-dot {
    width: 58px;
    height: 58px;
    border-radius: 50%;
    background: var(--orange);
  }
  .brand-name {
    font-size: 66px;
    font-weight: 500;
    letter-spacing: 12px;
    color: var(--light);
  }
</style>
</head>
<body>
<main class="sheet">
  <section class="card card-front">
    <div class="identity">
      <p class="person-name">Nome e Sobrenome</p>
      <p class="person-role">Cargo | Função</p>
    </div>
    <ul class="contact-list">
      <li class="contact-item">
        <svg class="contact-icon" viewBox="0 0 24 24" aria-hidden="true">
          <circle cx="12" cy="12" r="12" fill="#f28c1c"/>
          <path d="M8.5 6.5l2 2.2-1.2 1.4c.8 1.7 2 2.9 3.6 3.7l1.4-1.2 2.2 2-1 1.9c-4.3-.3-8.1-4.1-8.4-8.4z" fill="#fff"/>
        </svg>
        <span>(00) 0000-0000</span>
      </li>
      <li class="contact-item">
        <svg class="contact-icon" viewBox="0 0 24 24" aria-hidden="true">
          <circle cx="12" cy="12" r="12" fill="#f28c1c"/>
          <rect x="6" y="8" width="12" height="8.5" rx="1" fill="#fff"/>
          <path d="M6.5 8.6l5.5 4 5.5-4" stroke="#f28c1c" stroke-width="1.2" fill="none"/>
        </svg>
        <span>contato@exemplo.com</span>
      </li>
      <li class="contact-item">
        <svg class="contact-icon" viewBox="0 0 24 24" aria-hidden="true">
          <circle cx="12" cy="12" r="12" fill="#f28c1c"/>
          <circle cx="12" cy="12" r="6" fill="none" stroke="#fff" stroke-width="1.4"/>
          <ellipse cx="12" cy="12" rx="2.6" ry="6" fill="none" stroke="#fff" stroke-width="1.2"/>
          <line x1="6" y1="12" x2="18" y2="12" stroke="#fff" stroke-width="1.2"/>
        </svg>
        <span>www.exemplo.com.br</span>
      </li>
      <li class="contact-item">
        <svg class="contact-icon" viewBox="0 0 24 24" aria-hidden="true">
          <circle cx="12" cy="12" r="12" fill="#f28c1c"/>
          <path d="M12 5.5a4.5 4.5 0 0 0-4.5 4.5c0 3.4 4.5 8.5 4.5 8.5s4.5-5.1 4.5-8.5A4.5 4.5 0 0 0 12 5.5z" fill="#fff"/>
          <circle cx="12" cy="10" r="1.7" fill="#f28c1c"/>
        </svg>
        <span>rua exemplo, s/ 000<br>cidade-UF, CEP: 00000-000</span>
      </li>
    </ul>
    <div class="brand-accent" aria-hidden="true"></div>
  </section>

  <section class="card card-back">
    <div class="brand-lockup">
      <span class="brand-dot" aria-hidden="true"></span>
      <span class="brand-name">NUVARO</span>
    </div>
  </section>
</main>
</body>
</html>
```